Business card design for Velvet Harbor

We need business cards designed for our new marketing consulting company, Velvet Harbor. Our services include marketing strategy, go-to-market and launch planning, growth strategy, and execution. We serve medical technology and health technology companies, from startups to well-established growth companies.

The business cards should feel professional, credible, reliable and trustworthy, and should instill confidence. Also bold, creative, and modern.

The design must use the Velvet Harbor logo.

The primary brand color is this orange: #FF5501
A secondary color that you can use is this gray: #282B2D
I would prefer only to use the orange and gray. But if you feel you really need an additional accent color (please use it very sparingly, as little as possible), you can use this blue for small accent purposes: #009FED

Attached are the logo files. The main logo is the one with a little bit of orange on the left and the rest is gray.

The business card should include the following:

Velvet Harbor logo
First name and last name
Title
Email address
Phone number and type (in whatever order looks best for the design
Website (the website does not need to be in the same block as the personal info)

For example:

Nessa Pryle
Founder & Principal
nessa@velvetharbor.com
+1.628.309.4156 mobile (can use "." or spaces in between blocks of numbers)
velvetharbor.com (somewhere on the card, it does not need to be with the personal info; and note that there is no "www." at the beginning)

Note that there will be no address listed on the business card.

Target Market(s)

Executives (CEO, head of marketing, head of sales) at medical technology and health technology companies, mostly in their 40s and older, well-educated, often with advanced degrees. They are strategic thinkers, responsible for budgets, and familiar with P&L. Their comfort with and trust in using outside consultants varies.

Industry/Entity Type

Medical technology and health technology companies.

Contact Information for Business Card

See project description

Font styles to use
Sans Serif

Requirements
Must have
• Logo and see Business card details section above.

```html
<!DOCTYPE html>
<html lang="en">
<head>
<meta charset="utf-8">
<title>Velvet Harbor — Business Card</title>
<link rel="stylesheet" href="https://fonts.googleapis.com/css2?family=Montserrat:wght@400;500;600;700&display=swap">
<style>
  :root {
    --orange: #FF5501;
    --gray: #282B2D;
    --ink: #2a2c2e;
    --paper: #ffffff;
    --stage: #161718;
    --back-mark: #6a6f73;
  }
  * { box-sizing: border-box; margin: 0; padding: 0; }
  html, body { width: 1200px; height: 897px; overflow: hidden; }
  body {
    position: relative;
    background: var(--stage);
    font-family: "Montserrat", Arial, sans-serif;
  }
  .card {
    position: absolute;
    left: 303px;
    width: 595px;
    height: 338px;
    border-radius: 20px;
    overflow: hidden;
  }
  .card-front { top: 92px; background: var(--paper); }
  .card-back { top: 469px; background: var(--gray); }

  .brand {
    position: absolute;
    display: flex;
    align-items: center;
  }
  .brand-dot { border-radius: 50%; flex: none; }
  .brand-name {
    font-weight: 700;
    text-transform: uppercase;
    line-height: 1.05;
  }
  .card-front .brand { left: 128px; top: 40px; gap: 26px; }
  .card-front .brand-dot { width: 62px; height: 62px; background: var(--orange); }
  .card-front .brand-name { font-size: 31px; letter-spacing: 9px; color: var(--gray); }

  .card-back .brand { left: 98px; top: 128px; gap: 30px; }
  .card-back .brand-dot { width: 82px; height: 82px; background: var(--orange); }
  .card-back .brand-name { font-size: 40px; letter-spacing: 11px; color: var(--back-mark); }

  .band {
    position: absolute;
    left: 0; top: 172px;
    width: 100%; height: 74px;
    background: linear-gradient(to right, var(--gray) 0 297px, var(--orange) 297px 100%);
  }
  .band-circle {
    position: absolute;
    left: 255px; top: -5px;
    width: 84px; height: 84px;
    border-radius: 50%;
    background: var(--paper);
  }
  .person {
    position: absolute;
    right: 363px; top: 20px;
    text-align: right;
  }
  .person-name {
    color: var(--orange);
    font-weight: 700;
    font-size: 17px;
    letter-spacing: 3.5px;
    text-transform: uppercase;
    line-height: 1.1;
  }
  .person-title {
    color: #ffffff;
    font-size: 14px;
    font-weight: 500;
    letter-spacing: 0.4px;
    margin-top: 1px;
  }
  .contact {
    position: absolute;
    left: 358px; top: 11px;
    list-style: none;
    color: #ffffff;
    font-size: 13.5px;
    line-height: 18px;
    font-weight: 500;
  }
  .contact li { display: flex; align-items: center; gap: 3px; }
  .contact svg { width: 11px; height: 11px; flex: none; }

  .services {
    position: absolute;
    left: 0; top: 275px;
    width: 100%;
    text-align: center;
    color: var(--ink);
    font-size: 13.5px;
    line-height: 19px;
    font-weight: 500;
  }
  .services-label { color: var(--orange); font-weight: 600; margin-right: 6px; }
  .services-sep { color: var(--orange); margin: 0 8px; font-weight: 600; }
</style>
</head>
<body>
  <section class="card card-front" aria-label="Business card front">
    <div class="brand">
      <span class="brand-dot"></span>
      <span class="brand-name">Velvet<br>Harbor</span>
    </div>

    <div class="band">
      <div class="person">
        <p class="person-name">Nessa Pryle</p>
        <p class="person-title">Founder &amp; Principal</p>
      </div>
      <span class="band-circle"></span>
      <ul class="contact">
        <li>
          <svg viewBox="0 0 12 12" aria-hidden="true"><path d="M3 1 L5 3.5 L4 5 Q5 7 7 8 L8.5 7 L11 9 L9.5 11 Q5 11 2.5 7.5 Q1 5 1.5 2.5 Z" fill="none" stroke="#fff" stroke-width="1.1" stroke-linejoin="round"/></svg>
          +1.628.309.4156
        </li>
        <li>
          <svg viewBox="0 0 12 12" aria-hidden="true"><rect x="1" y="2.5" width="10" height="7" fill="none" stroke="#fff" stroke-width="1.1"/><path d="M1 2.5 L6 6.5 L11 2.5" fill="none" stroke="#fff" stroke-width="1.1"/></svg>
          nessa@velvetharbor.com
        </li>
        <li>
          <svg viewBox="0 0 12 12" aria-hidden="true"><circle cx="6" cy="6" r="5" fill="none" stroke="#fff" stroke-width="1"/><ellipse cx="6" cy="6" rx="2.2" ry="5" fill="none" stroke="#fff" stroke-width="1"/><path d="M1 6 H11 M2 3.5 H10 M2 8.5 H10" stroke="#fff" stroke-width="0.8"/></svg>
          www.velvetharbor.com
        </li>
      </ul>
    </div>

    <div class="services">
      <p><span class="services-label">Service :</span>marketing strategy</p>
      <p>go-to-market and launch planning<span class="services-sep">|</span>growth strategy, and execution</p>
    </div>
  </section>

  <section class="card card-back" aria-label="Business card back">
    <div class="brand">
      <span class="brand-dot"></span>
      <span class="brand-name">Velvet<br>Harbor</span>
    </div>
  </section>
</body>
</html>
```